Telecommunications Company needs a business card design

We are looking for a sleek, professional and modern business card design based off our new logo. Will look at both light and dark options. On some designs please provide a small space for a QR code

Target Market(s)

B2B clients in Australia

Contact Information for Business Card

Name, Position, Brisbane (head) office, Phone number, email address, QR code (link to our website brightlinktelco.com.au

Colors
0054AA
0677BA
7BADD7
CADEEF
E8F1F8
0094D4
00A9DD
6FCCEA
C7EBF8
E9F6FB
00AB8E
00BBA5
67D7C9
C6EFE9
E9F9F6

```html
<!DOCTYPE html>
<html lang="en">
<head>
<meta charset="utf-8">
<title>BrightLink Telco – Business Card</title>
<link href="https://fonts.googleapis.com/css2?family=Nunito+Sans:wght@300;400;700&display=swap" rel="stylesheet">
<style>
  :root {
    --stage: #e7e7e8;
    --paper: #ffffff;
    --ink-grey: #7d8088;
    --ink-soft: #9a9da4;
    --brand-blue: #0061ab;
    --brand-mid: #0677ba;
    --brand-teal: #00a6a6;
    --brand-green: #00bba5;
    --white: #ffffff;
  }
  * { box-sizing: border-box; margin: 0; padding: 0; }
  html, body {
    width: 1200px; height: 900px; overflow: hidden;
    background: var(--stage);
    font-family: "Nunito Sans", Arial, sans-serif;
  }
  .sheet {
    width: 1200px; height: 900px;
    display: flex; flex-direction: column; align-items: center; justify-content: center;
    gap: 56px;
  }
  .card {
    width: 600px; height: 343px;
    position: relative;
    border-radius: 2px;
    box-shadow: 0 10px 28px rgba(0,0,0,0.14), 0 2px 4px rgba(0,0,0,0.08);
    overflow: hidden;
  }
  /* Front: contact side */
  .card--front { background: var(--paper); }
  .brand-mark {
    position: absolute; left: 40px; top: 38px;
    display: flex; align-items: center; gap: 8px;
    font-weight: 700; font-size: 20px; letter-spacing: 0.5px;
    color: var(--brand-mid);
  }
  .brand-mark__dot {
    width: 12px; height: 12px; border-radius: 50%;
    background: var(--brand-green);
  }
  .person {
    position: absolute; left: 210px; top: 118px;
  }
  .person__name {
    font-weight: 300; font-size: 30px; letter-spacing: 1px;
    color: var(--ink-grey); line-height: 1;
  }
  .person__role {
    font-weight: 700; font-size: 14px; letter-spacing: 0.5px;
    color: var(--brand-green); margin-top: 2px;
  }
  .contact-list {
    position: absolute; left: 186px; top: 196px;
    list-style: none;
    display: flex; flex-direction: column; gap: 9px;
  }
  .contact-list__item {
    display: flex; align-items: center; gap: 12px;
    font-size: 14px; font-weight: 400; letter-spacing: 0.4px;
    color: var(--ink-soft);
  }
  .contact-list__icon { width: 14px; height: 14px; flex: none; }
  /* Back: brand side */
  .card--back {
    background: linear-gradient(90deg, var(--brand-blue) 0%, var(--brand-mid) 30%, #0092a8 62%, #0098a6 100%);
    display: flex; align-items: center; justify-content: center;
  }
  .brand-wordmark {
    margin-left: 18px;
    display: flex; align-items: center; gap: 12px;
    font-weight: 700; font-size: 34px; letter-spacing: 2px;
    color: var(--white);
  }
  .brand-wordmark__square {
    width: 18px; height: 18px; background: var(--white);
  }
</style>
</head>
<body>
  <main class="sheet">
    <section class="card card--front" aria-label="Business card front">
      <div class="brand-mark"><span class="brand-mark__dot"></span>BrightLink Telco</div>
      <div class="person">
        <p class="person__name">Name Surname</p>
        <p class="person__role">Position</p>
      </div>
      <ul class="contact-list">
        <li class="contact-list__item">
          <svg class="contact-list__icon" viewBox="0 0 14 14" aria-hidden="true"><path d="M7 1a4.5 4.5 0 0 0-4.5 4.5C2.5 9 7 13 7 13s4.5-4 4.5-7.5A4.5 4.5 0 0 0 7 1z" fill="#0094d4"/><circle cx="7" cy="5.5" r="1.7" fill="#fff"/></svg>
          27 Harbour Street, Kelvin Grove
        </li>
        <li class="contact-list__item">
          <svg class="contact-list__icon" viewBox="0 0 14 14" aria-hidden="true"><path d="M4 1.5l2 2.8-1.2 1.3c.7 1.6 2 2.9 3.6 3.6l1.3-1.2 2.8 2-1 2.2C6.5 12 2 7.5 1.8 2.5z" fill="#0094d4"/></svg>
          1300 555 214
        </li>
        <li class="contact-list__item">
          <svg class="contact-list__icon" viewBox="0 0 14 14" aria-hidden="true"><rect x="1" y="3" width="12" height="8.5" rx="1" fill="#0094d4"/><path d="M1.5 3.6L7 8l5.5-4.4" fill="none" stroke="#fff" stroke-width="1"/></svg>
          info@brightlinktelco.com.au
        </li>
        <li class="contact-list__item">
          <svg class="contact-list__icon" viewBox="0 0 14 14" aria-hidden="true"><circle cx="7" cy="7" r="6" fill="#0094d4"/><g fill="none" stroke="#fff" stroke-width="0.8"><ellipse cx="7" cy="7" rx="2.6" ry="6"/><path d="M1 7h12M2 4h10M2 10h10"/></g></svg>
          brightlinktelco.com.au
        </li>
      </ul>
    </section>

    <section class="card card--back" aria-label="Business card back">
      <div class="brand-wordmark"><span class="brand-wordmark__square"></span>BRIGHTLINK TELCO</div>
    </section>
  </main>
</body>
</html>
```